Building company buisness cards

We are looking for a sharp modern new look for our business cards.We are a New Zealand based company that specialises in house and land packages.We have attached a photo of the current logo and would like to see if it can be improved somehow if needed.We are open to any colours but we have chosen Black and White at this stage. Feel free to change the font and make the logo smarter looking.Play with the colours and see what looks best.We want a card that looks so good know one will want to throw it away!

Target Market(s)

Building profesonals, home buyers

Industry/Entity Type

Building

Contact Information for Business Card

Derek Haskins
0274930268
derekh@stonerange.co.nz

Font styles to use
Serif
Sans Serif

Colors

Designer to choose colors to be used in the design.

Requirements
Must have
• Just the logo on one side and details on the other
• Clean simple looking card
Nice to have
• Round corners and detail like raised or spot UV
• Something that stands out
Should not have
• To title needed, Director etc

```html
<!DOCTYPE html>
<html lang="en">
<head>
<meta charset="utf-8">
<title>Stonerange business cards</title>
<link rel="stylesheet" href="https://fonts.googleapis.com/css2?family=Oswald:wght@500&family=Work+Sans:wght@400;500&display=swap">
<style>
  :root {
    --backdrop: #bfe3d8;
    --card-white: #ffffff;
    --card-black: #0a0a0a;
    --ink: #111111;
    --ink-soft: #2a2a2a;
    --paper-text: #ffffff;
  }
  * { box-sizing: border-box; margin: 0; padding: 0; }
  html, body {
    width: 1200px;
    height: 856px;
    overflow: hidden;
    background: var(--backdrop);
  }
  .canvas {
    position: relative;
    width: 1200px;
    height: 856px;
  }
  .card {
    position: absolute;
    width: 560px;
    height: 320px;
    border-radius: 30px;
    box-shadow: 0 18px 40px rgba(40, 90, 80, 0.18);
  }

  /* Logo side */
  .card--logo {
    left: 540px;
    top: 90px;
    background: var(--card-black);
    display: flex;
    align-items: center;
    justify-content: center;
  }
  .brand__name {
    font-family: "Work Sans", sans-serif;
    font-weight: 500;
    font-size: 52px;
    letter-spacing: 0.5px;
    color: var(--paper-text);
  }

  /* Details side */
  .card--details {
    left: 100px;
    top: 440px;
    background: var(--card-white);
    color: var(--ink);
  }
  .identity {
    position: absolute;
    right: 310px;
    top: 124px;
    text-align: right;
  }
  .identity__name {
    font-family: "Oswald", sans-serif;
    font-weight: 500;
    font-size: 30px;
    letter-spacing: 1px;
    text-transform: uppercase;
    line-height: 1;
  }
  .divider {
    position: absolute;
    left: 272px;
    top: 108px;
    width: 2px;
    height: 62px;
    background: var(--ink);
  }
  .contact {
    position: absolute;
    left: 298px;
    top: 104px;
    list-style: none;
    font-family: "Work Sans", sans-serif;
    font-size: 15px;
    color: var(--ink-soft);
  }
  .contact__item {
    display: flex;
    align-items: center;
    gap: 9px;
    height: 22px;
  }
  .contact__icon {
    width: 11px;
    height: 11px;
    flex: none;
  }
  .address {
    position: absolute;
    left: 0;
    right: 0;
    bottom: 42px;
    text-align: center;
    font-family: "Work Sans", sans-serif;
    font-size: 15px;
    letter-spacing: 0.4px;
    color: var(--ink);
    padding-left: 90px;
  }
</style>
</head>
<body>
<main class="canvas">

  <section class="card card--logo" aria-label="Card back with company name">
    <span class="brand__name">Stonerange</span>
  </section>

  <section class="card card--details" aria-label="Card front with contact details">
    <div class="identity">
      <p class="identity__name">Derek Haskins</p>
    </div>

    <span class="divider" aria-hidden="true"></span>

    <ul class="contact">
      <li class="contact__item">
        <svg class="contact__icon" viewBox="0 0 12 12" aria-hidden="true">
          <path d="M3 1 L5 3.5 L4 5 Q5 7 7 8 L8.5 7 L11 9 L9.5 11 Q4 10.5 1 3 Z" fill="#111"/>
        </svg>
        <span>0274930268</span>
      </li>
      <li class="contact__item">
        <svg class="contact__icon" viewBox="0 0 12 12" aria-hidden="true">
          <rect x="1" y="2.5" width="10" height="7" fill="none" stroke="#111" stroke-width="1.2"/>
          <path d="M1 2.5 L6 6.5 L11 2.5" fill="none" stroke="#111" stroke-width="1.2"/>
        </svg>
        <span>derekh@stonerange.co.nz</span>
      </li>
      <li class="contact__item">
        <svg class="contact__icon" viewBox="0 0 12 12" aria-hidden="true">
          <circle cx="6" cy="6" r="5" fill="none" stroke="#111" stroke-width="1.1"/>
          <ellipse cx="6" cy="6" rx="2.2" ry="5" fill="none" stroke="#111" stroke-width="1"/>
          <line x1="1" y1="6" x2="11" y2="6" stroke="#111" stroke-width="1"/>
        </svg>
        <span>www.stonerange.co.nz</span>
      </li>
    </ul>

    <p class="address">142b Harlow Street, Christchurch, NZ, 8011</p>
  </section>

</main>
</body>
</html>
```